Real Estate Managemene Company Needs Business Card Design

We have a logo design and just need business cards made now for our business. Please use PDF logo # 3.

Card with Information to be attached shortly.

The card is used for a real estate management company. We will need to add four other employees and their cards.

Industry/Entity Type

Real Estate

Contact Information for Business Card

Tariq Hamdan
President
3187 Thornwick Avenue
Suite C
Glendale Heights, IL 60152
Phone 630.417.2286
Fax 630.417.2287
Cell 630.473.8062
vantorp@mailbreeze.net

Once design is approved we will have four other employees
Omar Hamdan
Operations Manager

Nadia Hamdan
Administrative Manager

Faz Hamdan
Principal

We would need to take out the cell # 630.473.8062 out for the remaining three cards.

Requirements
Must have
• Please use logo attached

```html
<!DOCTYPE html>
<html lang="en">
<head>
<meta charset="utf-8">
<title>Harborline Property Management Group – Business Cards</title>
<link rel="stylesheet" href="https://fonts.googleapis.com/css2?family=Open+Sans:wght@400;600;700&display=swap">
<style>
  :root {
    --backdrop: #3b3532;
    --card: #121314;
    --ink: #f4f4f4;
    --accent: #2f66b3;
    --rule: #5c5f63;
  }
  * { box-sizing: border-box; margin: 0; padding: 0; }
  html, body { width: 1200px; height: 814px; overflow: hidden; }
  body {
    background: var(--backdrop);
    font-family: "Open Sans", Arial, sans-serif;
    color: var(--ink);
    position: relative;
  }
  .card {
    position: absolute;
    width: 525px;
    height: 300px;
    background: var(--card);
    border-radius: 3px;
    box-shadow: 0 10px 26px rgba(0,0,0,.45);
  }
  .card--back { left: 45px; top: 257px; }
  .card--front { left: 630px; top: 257px; }

  .wordmark {
    display: flex;
    align-items: center;
    gap: 10px;
    color: var(--ink);
    font-weight: 600;
    text-transform: uppercase;
    letter-spacing: .06em;
    line-height: 1.25;
  }
  .wordmark__mark {
    flex: none;
    width: 14px;
    height: 14px;
    background: var(--accent);
  }
  .card--back .wordmark {
    position: absolute;
    left: 30px;
    top: 122px;
    width: 260px;
    font-size: 17px;
  }
  .card--front .wordmark {
    position: absolute;
    left: 0; right: 0;
    top: 118px;
    justify-content: center;
    font-size: 21px;
    padding: 0 40px;
  }

  .divider {
    position: absolute;
    left: 300px;
    top: 46px;
    width: 1px;
    height: 200px;
    background: var(--rule);
  }
  .contact {
    position: absolute;
    left: 320px;
    top: 50px;
    font-size: 13.5px;
    line-height: 1.5;
  }
  .contact__name {
    color: var(--accent);
    font-weight: 700;
    font-size: 15.5px;
  }
  .contact__lines { list-style: none; }
  .contact__lines li { display: flex; align-items: center; gap: 7px; }
  .icon { width: 11px; height: 11px; fill: var(--accent); flex: none; }
</style>
</head>
<body>
  <section class="card card--back" aria-label="Business card, contact side">
    <div class="wordmark">
      <span class="wordmark__mark"></span>
      <span>Harborline Property Management Group</span>
    </div>
    <div class="divider"></div>
    <div class="contact">
      <p class="contact__name">Tariq Hamdan</p>
      <p>President</p>
      <p>3187 Thornwick Avenue</p>
      <p>Suite C</p>
      <p>Glendale Heights, IL 60152</p>
      <ul class="contact__lines">
        <li>
          <svg class="icon" viewBox="0 0 12 12"><path d="M2.5 0.5l2 2.5-1.2 1.5c.8 1.7 2.3 3.2 4 4l1.5-1.2 2.5 2-1.2 2.2C5.5 11.2.8 6.5.3 1.7z"/></svg>
          630.417.2286
        </li>
        <li>
          <svg class="icon" viewBox="0 0 12 12"><rect x="3" y="0" width="6" height="12" rx="1"/><rect x="4" y="1.5" width="4" height="7" fill="#121314"/></svg>
          630.473.8062
        </li>
        <li>
          <svg class="icon" viewBox="0 0 12 12"><rect x="3" y="0" width="6" height="4"/><rect x="0" y="4" width="12" height="6" rx="1"/><rect x="3" y="8" width="6" height="4" fill="#121314" stroke="#2f66b3"/></svg>
          630.417.2287
        </li>
        <li>
          <svg class="icon" viewBox="0 0 12 12"><rect x="0" y="2" width="12" height="8"/><path d="M0 2l6 4.5L12 2" fill="none" stroke="#121314" stroke-width="1.2"/></svg>
          vantorp@mailbreeze.net
        </li>
      </ul>
    </div>
  </section>

  <section class="card card--front" aria-label="Business card, name side">
    <div class="wordmark">
      <span class="wordmark__mark"></span>
      <span>Harborline Property Management Group</span>
    </div>
  </section>
</body>
</html>
```